Webdesign für Birke Werkstatt
Zielgruppe
Birke Werkstatt produziert GfK Formteile und Abdeckungen
Einzelanfertigungen • Negativ - Formenbau • Prototyping • Ur-Modellbau
Formteile • Abdeckungen • Behälter • Sonderanfertigungen • Beschichtungen
Prototypen Modellbau • Anfertigung von Negativformen • Reparaturen • Fahrzeugteile
Hauptzielgruppe ist die Luftfahrtindustrie (Abdeckungen für Triebwerke)
Durch den Prototypenbau und die Einzelanfertigungen ist die Zielgruppe nicht klar zu definieren. Es werden Einzelteile jeglicher Art aus GfK hergestellt.
Dies können auch Anbauteile für PKW, Poolbeschichtungen, Teile für Boote etc sein.
Es gibt auch Kleinserien. Beispielsweise baut Birke-Werkstatt Motorhauben für Hallo-Brenner Rasenmähertrecker aus den 70er Jahren nach, die es nicht mehr zu kaufen gibt.
Aufgabenstellung
Der Designer hat alle Freiheiten. Die Seite muss natürlich responsiv funktionieren.
Außer dem Logo gibt es keine must-haves.
Schriftart aus dem Logo: EXO 2

```html
<!DOCTYPE html>
<html lang="de">
<head>
<meta charset="utf-8">
<title>Birke Werkstatt – GfK-Formteile & Ur-Modellbau</title>
<link rel="stylesheet" href="https://fonts.googleapis.com/css2?family=Exo+2:wght@400;700&family=Lato:wght@400;700&family=Roboto:wght@300;400;500;700&family=Roboto+Condensed:wght@400;700&display=swap">
<style>
:root{
  --blue:#0b67a8;
  --blue-dark:#08548c;
  --ink:#333;
  --muted:#666;
  --light:#f1f1f3;
  --footer:#47474b;
  --nav-active:#3c3c3f;
  --white:#fff;
}
*{box-sizing:border-box;margin:0;padding:0}
html,body{width:1200px;height:2654px;overflow:hidden}
body{font-family:"Roboto",sans-serif;color:var(--ink);background:var(--white);position:relative}
a{color:inherit}

/* header */
.site-header{position:absolute;top:0;left:0;width:1200px;height:99px;background:var(--white)}
.brand{position:absolute;left:70px;top:22px;display:flex;align-items:center;gap:12px}
.brand-mark{width:46px;height:46px;background:var(--blue)}
.brand-name{font-family:"Exo 2",sans-serif;font-weight:700;font-size:33px;color:var(--blue);line-height:1}
.brand-tag{position:absolute;left:58px;top:44px;font-family:"Exo 2",sans-serif;font-size:11px;color:var(--muted);white-space:nowrap}
.contact-item{position:absolute;top:34px;display:flex;gap:10px;font-size:12px;line-height:18px;color:#444}
.contact-item svg{width:24px;height:24px;flex:none;margin-top:3px}
.contact-item b{font-weight:500;color:#222}

/* nav */
.main-nav{position:absolute;top:99px;left:0;width:1200px;height:53px;background:var(--blue);display:flex;padding-left:69px}
.main-nav a{font-family:"Roboto Condensed",sans-serif;font-weight:700;letter-spacing:.9px;font-size:13px;color:var(--white);text-decoration:none;line-height:53px;padding:0 14px;white-space:nowrap}
.main-nav a.active{background:var(--nav-active)}

/* hero */
.hero{position:absolute;top:152px;left:0;width:1200px;height:470px;background:linear-gradient(180deg,#8c8e90 0%,#b3b4b3 45%,#6e6f6a 75%,#3f403c 100%)}
.slide-arrow{position:absolute;width:37px;height:37px;display:flex;align-items:center;justify-content:center}
.slide-arrow.outline{border:2px solid rgba(255,255,255,.8)}
.slide-arrow.filled{background:rgba(60,60,60,.75)}

/* welcome */
.welcome{position:absolute;top:622px;left:0;width:1200px;height:109px;text-align:center}
.welcome h1{font-family:"Lato",sans-serif;font-weight:400;font-size:28px;color:#3b3b3b;margin-top:11px}
.welcome p{font-family:"Lato",sans-serif;font-size:14px;color:#555;margin-top:2px}
.welcome-band{position:absolute;left:0;bottom:0;width:1200px;height:40px;background:linear-gradient(180deg,#ffffff 0%,#ececee 100%)}

/* features */
.features{position:absolute;top:731px;left:0;width:1200px;height:406px;background:var(--light)}
.feature{position:absolute;top:29px;width:294px;height:327px;background:var(--white)}
.feature .thumb{height:178px}
.feature h3{font-size:13px;font-weight:700;color:#222;margin:24px 8px 0}
.feature p{font-size:12px;line-height:18px;color:#777;margin:16px 8px 0}

/* services */
.services{position:absolute;top:1137px;left:0;width:1200px;height:394px;background:linear-gradient(135deg,#0a5f9e,#0f6db0 50%,#0a5a96);text-align:center;color:var(--white)}
.services h2{font-family:"Lato",sans-serif;font-weight:700;font-size:25px;margin-top:33px}
.services p{font-family:"Lato",sans-serif;font-size:14px;line-height:20px;margin-top:6px}
.services p strong{font-family:"Exo 2",sans-serif;font-size:18px;font-weight:700}
.service{position:absolute;top:145px;width:297px;height:200px;text-align:left}
.service h4{position:absolute;left:25px;top:118px;font-size:13px;font-weight:700;color:var(--white)}
.service .btn{position:absolute;left:25px;top:143px;background:var(--blue);font-size:12px;font-weight:700;padding:7px 9px;color:var(--white)}

/* competence */
.competence{position:absolute;top:1531px;left:0;width:1200px;height:361px;background:repeating-linear-gradient(135deg,#f3f3f3 0 3px,#ececec 3px 5px)}
.competence h2{text-align:center;font-weight:700;font-size:25px;color:#3a3a3a;margin-top:41px}
.competence .lead{text-align:center;font-weight:300;font-size:15px;color:#555;margin-top:4px}
.cat{position:absolute;font-size:13px;font-weight:700;color:#3a3a3a}
.cat::after{content:"";display:block;width:38px;height:3px;background:#c9c9c9;margin-top:12px}
.tags{position:absolute;display:flex;flex-wrap:wrap;font-size:12px;color:#555;column-gap:18px;row-gap:11px}
.tags span::before{content:"";display:inline-block;width:4px;height:4px;background:#bbb;margin-right:5px;vertical-align:middle}

/* news */
.news{position:absolute;top:1892px;left:0;width:1200px;height:400px}
.news h2{text-align:center;font-weight:700;font-size:24px;color:#3a3a3a;margin-top:20px}
.post{position:absolute;top:80px;width:278px}
.post .thumb{height:141px}
.post .rule{width:38px;height:3px;background:#c9c9c9;margin-top:24px}
.post h3{font-size:13px;font-weight:500;letter-spacing:.3px;margin-top:11px;color:#333}
.post p{font-size:11px;line-height:15px;color:#555;margin-top:2px}
.post .meta{display:flex;align-items:center;gap:16px;margin-top:8px}
.post .btn{background:#3c3c3f;color:var(--white);font-size:11px;font-weight:700;padding:10px 9px}
.post time{font-size:10px;color:#999;display:flex;align-items:center;gap:6px}

/* footer */
.site-footer{position:absolute;top:2292px;left:0;width:1200px;height:278px;background:var(--footer);color:var(--white)}
.site-footer h5{position:absolute;top:50px;font-size:13px;font-weight:700}
.about{position:absolute;left:138px;top:88px;width:325px;font-size:10px;line-height:18px}
.socials{position:absolute;left:140px;top:210px;display:flex;gap:14px}
.socials span{width:15px;height:15px;border-radius:50%;background:var(--white)}
.f-contact{position:absolute;left:538px;display:flex;gap:20px;font-size:10px;line-height:13px}
.f-contact svg{width:15px;height:15px;flex:none}
.links{position:absolute;top:88px;font-size:10px;line-height:31.5px}
.links a{display:block;text-decoration:underline}
.copyright{position:absolute;top:2570px;left:0;width:1200px;height:84px;background:var(--blue);color:var(--white);font-size:12px;padding:38px 0 0 139px}
</style>
</head>
<body>

<header class="site-header">
  <div class="brand">
    <span class="brand-mark"></span>
    <span class="brand-name">Birke Werkstatt</span>
    <span class="brand-tag">GfK Formteile | Ur-Modellbau | Prototyping</span>
  </div>
  <div class="contact-item" style="left:566px">
    <svg viewBox="0 0 24 24" fill="none" stroke="#0b67a8" stroke-width="1.6"><path d="M5 3l4 4-2 3c1 3 4 6 7 7l3-2 4 4-3 3C10 22 2 14 2 6z"/><path d="M14 4a6 6 0 016 6M14 8a2 2 0 012 2"/></svg>
    <div><b>+49 511 / 720 41 18</b><br>info [a] birke-werkstatt.de</div>
  </div>
  <div class="contact-item" style="left:736px">
    <svg viewBox="0 0 24 24" fill="none" stroke="#0b67a8" stroke-width="1.6"><path d="M12 22s-7-8-7-13a7 7 0 0114 0c0 5-7 13-7 13z"/><circle cx="12" cy="9" r="2.5"/></svg>
    <div><b>GESCHAFTSFUHRER: K.HARTMANN</b><br>Lindenweg 14 30982 Wiesental</div>
  </div>
  <div class="contact-item" style="left:1008px">
    <svg viewBox="0 0 24 24" fill="none" stroke="#0b67a8" stroke-width="1.6"><circle cx="12" cy="12" r="9"/><path d="M12 6v6l-4 2"/></svg>
    <div><b>7:30 AM - 7:30 PM</b><br>Monday to Saturday</div>
  </div>
</header>

<nav class="main-nav">
  <a class="active" href="#">HOME</a>
  <a href="#">ÜBER UNS</a>
  <a href="#">LUFTFAHRT FORMTEILE</a>
  <a href="#">JET ENGINE COVER/PLUGS</a>
  <a href="#">AUFBLASBARE SONDERABDECKUNGEN</a>
  <a href="#">FORMBAUTEILE</a>
  <a href="#">REPARATURSERVICE</a>
</nav>

<section class="hero" role="img" aria-label="Verkehrsflugzeug auf dem Vorfeld mit gelben Triebwerksabdeckungen">
  <div class="slide-arrow outline" style="left:48px;top:202px"><svg width="12" height="16" viewBox="0 0 12 16"><path d="M9 2L3 8l6 6" fill="none" stroke="#fff" stroke-width="2.5"/></svg></div>
  <div class="slide-arrow filled" style="left:1115px;top:202px"><svg width="12" height="16" viewBox="0 0 12 16"><path d="M3 2l6 6-6 6" fill="none" stroke="#fff" stroke-width="2.5"/></svg></div>
</section>

<section class="welcome">
  <h1>WILLKOMMEN BEI BIRKE-WERKSTATT</h1>
  <p>Gfk-Formteile &amp; Ur-Modellbau &amp; Prototyping</p>
  <div class="welcome-band" role="img" aria-label="Dekorativer Übergangsstreifen"></div>
</section>

<section class="features">
  <article class="feature" style="left:137px">
    <div class="thumb" role="img" aria-label="Werkhalle mit großem GfK-Formteil" style="background:linear-gradient(160deg,#7fa8b4,#2f6e5f 50%,#3a2a22)"></div>
    <h3>AKTIVE WELTWEITE KOMPETENZ</h3>
    <p>Lorem ipsum dolor sit amet, consectetur adipiscing elit, sed do eiusmod tempor incididunt ut labore et dolore magna aliqua.</p>
  </article>
  <article class="feature" style="left:453px">
    <div class="thumb" role="img" aria-label="Hände in Handschuhen bearbeiten ein weißes Formteil" style="background:linear-gradient(160deg,#1f4d8e,#d9dadc 60%,#b9bcc0)"></div>
    <h3>FERTIGUNGSVERFAHREN</h3>
    <p>Lorem ipsum dolor sit amet, consectetur adipiscing elit, sed do eiusmod tempor incididunt ut labore et dolore magna aliqua.</p>
  </article>
  <article class="feature" style="left:770px">
    <div class="thumb" role="img" aria-label="Hand hält ein kleines blaues Bauteil" style="background:linear-gradient(160deg,#2d5f8f,#6b7d8a 55%,#c79b84)"></div>
    <h3>DOKUMENTATION / QUALITÄTSSICHERUNG</h3>
    <p>Lorem ipsum dolor sit amet, consectetur adipiscing elit, sed do eiusmod tempor incididunt ut labore et dolore magna aliqua.</p>
  </article>
</section>

<section class="services">
  <h2>UNSERE DIENSTLEISTUNGEN</h2>
  <p>Wir entwickeln und produzieren hochwertige faserverstärkte <strong>GfK-Formteile</strong> für<br>jede Art von Anwendungen. Es gibt beinahe nichts was wir nicht für Sie anfertigen können.</p>
  <div class="slide-arrow outline" style="left:49px;top:215px"><svg width="12" height="16" viewBox="0 0 12 16"><path d="M9 2L3 8l6 6" fill="none" stroke="#fff" stroke-width="2.5"/></svg></div>
  <div class="slide-arrow filled" style="left:1121px;top:216px;background:#0a5a96"><svg width="12" height="16" viewBox="0 0 12 16"><path d="M3 2l6 6-6 6" fill="none" stroke="#3d8ccc" stroke-width="2.5"/></svg></div>
  <div class="service" style="left:136px;background:linear-gradient(150deg,#5b5347,#8f2b2b 50%,#3a332b)" role="img" aria-label="Triebwerk mit roter Abdeckung">
    <h4>LUFTFAHRT FORMBAUTEILE</h4><span class="btn">MEHR SEHEN</span>
  </div>
  <div class="service" style="left:452px;background:linear-gradient(150deg,#4d4d4b,#a35b2e 50%,#555)" role="img" aria-label="Große orangefarbene GfK-Figur eines Insekts">
    <h4>FORMBAUTEILE</h4><span class="btn">MEHR SEHEN</span>
  </div>
  <div class="service" style="left:768px;background:linear-gradient(150deg,#77786f,#868985 50%,#6a6962)" role="img" aria-label="Beschichtetes Becken im Garten">
    <h4>REPARATURSERVICE</h4><span class="btn">MEHR SEHEN</span>
  </div>
</section>

<section class="competence">
  <h2>Gern bieten wir Ihnen unsere Leistungen und Kompetenz an</h2>
  <p class="lead">zur Realisierung Ihrer Wünsche oder&nbsp; Produkte in höchster Qualität mit herausragenden Oberflächen- und Materialeigenschaften.</p>
  <div class="cat" style="left:137px;top:144px">EINZELANFERTIGUNGEN</div>
  <div class="cat" style="left:373px;top:144px">NEGATIV - FORMENBAU</div>
  <div class="cat" style="left:609px;top:144px">PROTOTYPING</div>
  <div class="cat" style="left:845px;top:144px">UR-MODELLBAU</div>
  <div class="tags" style="left:137px;top:191px;width:1000px">
    <span>Formteile</span><span>Abdeckungen</span><span>Behälter</span><span>Sonderanfertigungen</span><span>Beschichtungen</span><span>Prototypen Modellbau</span><span>Anfertigung von Negativformen</span>
  </div>
  <div class="tags" style="left:137px;top:216px">
    <span>Reparaturen</span><span>Fahrzeugteile</span>
  </div>
  <div class="cat" style="left:137px;top:265px">FLUGZEUGE &amp; TRIEBWERKE / AIRCRAFTS &amp; OFF LINK JET ENGINES</div>
  <div class="tags" style="left:137px;top:313px">
    <span>Engine Cover</span><span>Triebwerk-Abdeckungen</span><span>Abdeckplanen</span><span>Engine Plugs</span><span>Transporttaschen</span>
  </div>
</section>

<section class="news">
  <h2>News</h2>
  <article class="post" style="left:137px">
    <div class="thumb" role="img" aria-label="Triebwerkseinlass mit Prüfgerät" style="background:linear-gradient(160deg,#2a2a2a,#c9c4b3 50%,#3a3a34)"></div>
    <div class="rule"></div>
    <h3>SED UT PERSPICIATIS</h3>
    <p>omnis iste natus error sit voluptatem accusantium doloremque laudantium, totam rem aperiam ...</p>
    <div class="meta"><span class="btn">MEHR SEHEN</span><time><svg width="11" height="11" viewBox="0 0 12 12" fill="none" stroke="#999" stroke-width="1.4"><circle cx="6" cy="6" r="5"/><path d="M6 3v3l2 1"/></svg>March 18, 2015</time></div>
  </article>
  <article class="post" style="left:462px">
    <div class="thumb" role="img" aria-label="Armaturenbrett-Formteil aus GfK" style="background:linear-gradient(160deg,#b5b1aa,#dcd9d3 50%,#6b655c)"></div>
    <div class="rule"></div>
    <h3>SED UT PERSPICIATIS</h3>
    <p>omnis iste natus error sit voluptatem accusantium doloremque laudantium, totam rem aperiam ...</p>
    <div class="meta"><span class="btn">MEHR SEHEN</span><time><svg width="11" height="11" viewBox="0 0 12 12" fill="none" stroke="#999" stroke-width="1.4"><circle cx="6" cy="6" r="5"/><path d="M6 3v3l2 1"/></svg>March 18, 2015</time></div>
  </article>
  <article class="post" style="left:786px">
    <div class="thumb" role="img" aria-label="Triebwerk mit gelber Abdeckung" style="background:linear-gradient(160deg,#3a3a3a,#b99030 45%,#8d8a86)"></div>
    <div class="rule"></div>
    <h3>SED UT PERSPICIATIS</h3>
    <p>omnis iste natus error sit voluptatem accusantium doloremque laudantium, totam rem aperiam ...</p>
    <div class="meta"><span class="btn">MEHR SEHEN</span><time><svg width="11" height="11" viewBox="0 0 12 12" fill="none" stroke="#999" stroke-width="1.4"><circle cx="6" cy="6" r="5"/><path d="M6 3v3l2 1"/></svg>March 18, 2015</time></div>
  </article>
</section>

<footer class="site-footer">
  <h5 style="left:138px">ÜBER UNS</h5>
  <p class="about">Wir entwickeln und fertigen geometrisch anspruchsvolle Formteile von höchster Qualität. Die von uns konzipierten Verbundwerkstoffe mit ihren herausragenden Oberflächen- und Materialeigenschaften bieten konstruktive Vorteile und erweitern die gestalterischen Möglichkeiten.</p>
  <div class="socials"><span></span><span></span><span></span></div>

  <h5 style="left:538px">GESCHÄFTSFÜHRER: K.HARTMANN</h5>
  <div class="f-contact" style="top:90px"><svg viewBox="0 0 16 16" fill="#fff"><path d="M8 1L0 8h2v7h4v-5h4v5h4V8h2z"/></svg><span>Lindenweg 14<br>30982 Wiesental Niedersachsen Deutschland</span></div>
  <div class="f-contact" style="top:140px"><svg viewBox="0 0 16 16"><rect width="16" height="16" rx="3" fill="#fff"/><path d="M5 3l2 2-1 2c1 2 2 3 3 3l1-1 2 2-1 2C7 13 3 9 3 5z" fill="#47474b"/></svg><span>+49 511 720 41 18</span></div>
  <div class="f-contact" style="top:181px"><svg viewBox="0 0 16 16" fill="#fff"><rect x="1" y="5" width="14" height="10" rx="1"/><rect x="4" y="1" width="8" height="5" fill="#fff" stroke="#47474b"/><path d="M4 9h2M8 9h2M4 12h2M8 12h2" stroke="#47474b"/></svg><span>+49 511 720 41 19</span></div>
  <div class="f-contact" style="top:217px"><svg viewBox="0 0 16 16" fill="#fff"><rect x="1" y="3" width="14" height="10"/><path d="M1 3l7 6 7-6" fill="none" stroke="#47474b" stroke-width="1.4"/></svg><span>info[a]birke-werkstatt.de</span></div>

  <h5 style="left:839px">SCHNELLZUGRIFF</h5>
  <div class="links" style="left:839px"><a href="#">Home</a><a href="#">Über uns</a><a href="#">Luftfahrt Formbauteile</a><a href="#">JetEngine Cover/Plugs</a><a href="#">Aufblasbare Sonderabdeckungen</a></div>
  <div class="links" style="left:992px"><a href="#">Formbauteile</a><a href="#">Reparaturservice</a><a href="#">Kontakt</a><a href="#">Impressum</a></div>
</footer>

<div class="copyright">Copyright © 2017 Birke-Werkstatt</div>

</body>
</html>
```